Maren Holt Luxury Wellness Profile Booklet

I am a luxury wellness property agent and would like to create my personal profile booklet. I want this to feel luxurious, minimalist, informative and the philosophy behind wellness and property the cPAGE 1 — THE COVER

Very minimal.

MAREN HOLT

LUXURY WELLNESS PROPERTY

PROPERTY • WELLNESS • LIFESTYLE

Fenwick Dale Coastline Group

Large photograph of you — preferably walking through a beautiful waterfront property or standing naturally within an architectural setting.

At the bottom:

Hope Island • Sanctuary Cove • Helensvale

Small Fenwick Dale logo.

PAGE 2 — THE OPENING STATEMENT

A beautiful full-page lifestyle photograph.

Overlaid:

WHERE PROPERTY
MEETS WELLBEING

“A home is more than an address. It is the environment in which life unfolds.”

Then a short introduction:

Opening Profile

I believe the most exceptional properties are not defined simply by their architecture, address or price.

They are defined by how they make you feel.

Natural light. Water views. Privacy. Green space. Indoor-outdoor living. A place to unwind, entertain, recharge and reconnect.

My approach to luxury property brings these elements together — combining strategic real estate expertise with a genuine understanding of wellness, lifestyle and the way people want to live today.

Because when we understand the lifestyle behind the property, we can create a more compelling story around it.

PAGE 3 — MEET MAREN

Large portrait of you on one side.

Other side:

MEET MAREN

20+ YEARS OF PROPERTY EXPERIENCE

Commercial
Residential
Project Sales
Luxury & Lifestyle Property

Then:

About Maren

With more than 20 years' experience across commercial, residential and project sales, I have built my career around relationships, strategic marketing and delivering exceptional outcomes for my clients.

My approach is warm, considered and highly personal.

I believe sellers deserve more than a listing campaign. They deserve a clear strategy, honest communication and an agent who understands what makes their property valuable — both financially and emotionally.

Today, my focus is luxury lifestyle property across the Northern Gold Coast, with a particular passion for Hope Island, Sanctuary Cove and selected waterfront gated estates in Helensvale.

PAGE 4 — WHY WELLNESS?

This is where your differentiation becomes really powerful.

Full-bleed photograph of:

pool
outdoor entertaining
greenery
water
spa
wellness room
person walking beside water
WELLNESS IS THE NEW LUXURY

Then:

Wellness Philosophy

Luxury has evolved.

Today, luxury is not only about beautiful finishes, expansive living spaces or an impressive address.

It is privacy.

It is waking to water.

It is natural light flooding through the home.

It is having space to breathe.

It is stepping outside into nature, walking along the water, enjoying a morning swim, entertaining beside the pool or creating a private sanctuary at home.

These lifestyle elements increasingly shape the way buyers experience and value a property.

This is where my passion for wellness becomes part of my property approach.

PAGE 5 — MY WELLNESS JOURNEY

This page makes the wellness positioning credible rather than simply being a marketing slogan.

MY WELLNESS JOURNEY

You could use 3 small photographs:

BLOOMTOT CO
SOLACE WELLNESS CENTRE
LUXURY WELLNESS PROPERTY

Copy:

Wellness Journey

My connection with wellness began outside of real estate.

After stepping away from property, I founded Bloomtot Co, developing an organic children's nutritional product with a focus on natural ingredients and wellbeing.

I later launched Solace Wellness Centre, further deepening my understanding of wellness, health-conscious lifestyles and the importance of creating environments that support how we live.

Today, I bring that perspective back into property.

I see homes differently — not simply as buildings, but as environments for living, restoring, entertaining and thriving.

PAGE 6 — THE MAREN HOLT DIFFERENCE

This should be one of your strongest pages.

A DIFFERENT WAY OF SEEING PROPERTY

Use six elegant icons or small images:

01 — LIFESTYLE

I look beyond the floor plan to understand how buyers will actually experience the home.

02 — WELLNESS

I identify the spaces and features that contribute to wellbeing and lifestyle.

03 — PRESENTATION

I create a campaign that makes the property feel aspirational, memorable and emotionally engaging.

04 — STORY

Every exceptional property has a story. I find it, refine it and communicate it.

05 — STRATEGY

From positioning and buyer targeting to campaign execution and negotiation, every element has a purpose.

06 — RELATIONSHIPS

Trust, transparency and communication remain at the centre of every campaign.

PAGE 7 — YOUR PROPERTY STORY

This could be a beautiful editorial spread.

EVERY HOME HAS A STORY

Then:

My role is to discover what makes yours extraordinary.

Three questions:

WHAT MAKES YOUR PROPERTY DIFFERENT?

Architecture?
Waterfront?
Views?
Privacy?
Garden?
Location?

HOW DOES IT MAKE PEOPLE FEEL?

Calm?
Inspired?
Connected?
Entertained?
Relaxed?

WHO WILL FALL IN LOVE WITH IT?

Families?
Executives?
Downsizers?
Boaties?
Golfers?
Wellness-focused buyers?
Lifestyle purchasers?

Then:

I turn these answers into your property's story.

PAGE 8 — YOUR NORTHERN GOLD COAST

Beautiful aerial/waterfront image.

MY MARKET

HOPE ISLAND

SANCTUARY COVE

HELENSVALE

WATERFRONT & GATED ESTATES

Copy:

Northern Gold Coast

I specialise in the lifestyle-driven property market of the Northern Gold Coast.

From the waterfront homes and private enclaves of Hope Island and Sanctuary Cove to the established gated estates of Helensvale, I understand the lifestyle characteristics that attract buyers to this part of the Gold Coast.

Having personally experienced the lifestyle of these communities, I understand that buyers are often purchasing far more than a house.

They are buying a way of life.

PAGE 9 — THE WELLNESS PROPERTY

This could become your signature page.

WHAT MAKES A WELLNESS HOME?

Use a sophisticated grid:

WATER
Pools • Waterfront • Marina • Water views

NATURE
Green space • Gardens • Reserve outlooks • Walking trails

LIGHT
Natural light • Orientation • Open spaces

MOVEMENT
Walking • Golf • Boating • Outdoor living

RESTORATION
Spa • Sauna • Cold plunge • Retreat spaces

CONNECTION
Entertaining • Family • Indoor/outdoor living

Bottom:

The most desirable luxury is often the way a home makes you feel.

PAGE 10 — THE SELLING EXPERIENCE
YOUR HOME. YOUR STORY. YOUR CAMPAIGN.

I would make this a simple six-stage journey:

01 — DISCOVER
Understand your property, your goals and your lifestyle.

↓

02 — POSITION
Establish the property's unique market position.

↓

03 — PREPARE
Presentation, styling and strategic recommendations.

↓

04 — CREATE
Photography, film, editorial storytelling and digital marketing.

↓

05 — CONNECT
Targeted buyer engagement and database activation.

↓

06 — NEGOTIATE
Strategic negotiation designed to maximise the opportunity.

PAGE 11 — THE POWER OF PRESENTATION

Large before/after style photography.

FIRST IMPRESSIONS ARE EVERYTHING

Copy:

We don't get a second opportunity to create a first impression.

Then explain your approach to:

styling
photography
cinematic video
twilight imagery
aerial photography
lifestyle storytelling
digital advertising
targeted database marketing
buyer follow-up
auction strategy

Importantly, don't make this page feel like a generic list of marketing products.

Frame everything around:

Creating desire before creating urgency.
PAGE 12 — PROVEN RESULTS

Now introduce your actual results.

RESULTS THAT BUILD CONFIDENCE

Use your strongest results as elegant case studies.

For example:
4183 Palmetto Drive, Hope Island
$3,850,000
34 Days On The Market

$2.90M
71 Heron Bay Boulevard, Helensvale
Sold within 45 days

Include your result and the property's story.

$2.15M

3/9 Heron Bay Boulevard

Waterfront Villa

Then potentially:

28 DAYS

5419 Quaywood Boulevard, Hope Island

Under contract following relaunch

If a result subsequently changed because the contract fell through, be careful about how you describe the current status. We can make this page completely accurate to the final outcome.

PAGE 13 — THE FENWICK DALE ADVANTAGE

This is where you let the brand support you, rather than letting the booklet become a Fenwick Dale corporate brochure.

PERSONAL SERVICE.
NATIONAL REACH.

Then a short statement about your Fenwick Dale platform.

You could include:

POWERFUL BUYER DATABASE

LUXURY PROPERTY MARKETING

AUCTION EXPERTISE

DIGITAL REACH

LOCAL KNOWLEDGE

NATIONAL NETWORK

And a short line:

The personal attention of a specialist agent, supported by the strength of a globally recognised property network.

PAGE 14 — WHAT YOU CAN EXPECT FROM ME

This page is very important for your seller proposition.

MY PROMISE TO YOU

TRANSPARENCY

Clear advice, honest feedback and no unnecessary promises.

COMMUNICATION

You will know what is happening throughout your campaign.

STRATEGY

Every decision is made with your property, market and objectives in mind.

ATTENTION TO DETAIL

Your home deserves meticulous preparation and presentation.

PERSONAL SERVICE

You deal directly with me throughout your campaign.

RESULT FOCUS

My role is to create the strongest possible environment for a successful sale.

PAGE 15 — THE CLOSING PAGE

This should be very luxurious and emotional.

Beautiful photograph of water at sunset / luxury pool / Hope Island lifestyle.

YOUR HOME.
YOUR NEXT CHAPTER.

Then:

Closing Statement

Selling a home is rarely just a transaction.

It is the closing of one chapter and the beginning of another.

My role is to make the journey feel considered, strategic and personal — while creating the strongest possible opportunity for your property in the marketplace.

Thank you for considering me to represent your home.

I would be honoured to tell its story.

Then your details:

MAREN HOLT

Luxury Wellness Property

0412 557 830

BACK COVER

Keep it extremely clean.

Your photograph or perhaps a beautiful Gold Coast waterfront image.

MAREN HOLT

LUXURY WELLNESS PROPERTY

0412 557 830

Fenwick Dale logoollaboration. I can send a full brief if required.

Target Market(s)

Luxury Property Owners

Industry/Entity Type

Wellness Luxury Real Estate Lifestyle

Requirements
Must have
• A luxurious minimalist clean feel

```html
<!DOCTYPE html>
<html lang="en">
<head>
<meta charset="utf-8">
<title>Maren Holt — Luxury Wellness Profile</title>
<link rel="stylesheet" href="https://fonts.googleapis.com/css2?family=Cormorant+Garamond:wght@400;500&family=Montserrat:wght@400;500;600;700&display=swap">
<style>
  :root {
    --backdrop: #221e17;
    --forest: #3c4a42;
    --forest-veil: rgba(54, 68, 60, 0.9);
    --gold: #b9955f;
    --cream: #f5f2eb;
    --ink: #1f1f1c;
    --white: #ffffff;
    --paper-edge: #f7f7f4;
  }
  * { box-sizing: border-box; margin: 0; padding: 0; }
  html, body { width: 1196px; height: 1200px; overflow: hidden; background: var(--backdrop); }
  .spread { position: relative; width: 1196px; height: 1200px; }
  .page {
    position: absolute; top: 366px; width: 330px; height: 467px; overflow: hidden;
    font-family: "Montserrat", sans-serif;
    box-shadow: 0 6px 18px rgba(0,0,0,0.45);
  }
  .page--cover { left: 92px; }
  .page--opening { left: 433px; }
  .page--meet { left: 774px; background: var(--cream); }

  .photo { position: absolute; inset: 0; }
  .photo--agent-walking { background: linear-gradient(100deg, #8d8c86 0%, #cfc8bd 45%, #efece6 70%, #f7f5f0 100%); }
  .photo--waterfront { background: linear-gradient(180deg, #b9c3c9 0%, #7d8c7a 28%, #3e5340 45%, #556b63 60%, #4f7f8c 78%, #3f6f80 100%); }
  .photo--agent-seated { left: 182px; background: linear-gradient(180deg, #e9e4dc 0%, #ddd4c8 55%, #cdbfae 100%); }

  .veil { position: absolute; top: 0; bottom: 0; left: 0; background: var(--forest-veil); }
  .page--cover .veil { width: 157px; }
  .page--opening .veil { width: 173px; }
  .page-edge { position: absolute; top: 0; bottom: 0; left: 0; width: 4px; background: var(--paper-edge); }

  .eyebrow {
    display: flex; align-items: center; gap: 5px;
    font-size: 4.6px; letter-spacing: 0.18em; font-weight: 600; color: var(--gold); text-transform: uppercase;
  }
  .eyebrow::before { content: ""; width: 12px; height: 0.6px; background: var(--gold); }

  .display {
    font-family: "Cormorant Garamond", serif; font-weight: 400; color: var(--white);
    text-transform: uppercase; line-height: 0.95; letter-spacing: 0.01em;
  }
  .rule { width: 22px; height: 0.8px; background: var(--gold); }

  /* cover */
  .cover-content { position: absolute; left: 24px; top: 33px; width: 130px; }
  .cover-content .display { font-size: 21px; margin-top: 30px; }
  .cover-content .rule { margin-top: 11px; }
  .cover-tagline { margin-top: 10px; font-size: 4.4px; letter-spacing: 0.2em; color: var(--white); font-weight: 500; }
  .pillars { margin-top: 13px; display: flex; gap: 9px; font-size: 4px; letter-spacing: 0.18em; color: var(--white); }
  .pillars span + span::before { content: "•"; margin-right: 6px; color: var(--gold); }
  .cover-footer { position: absolute; left: 24px; bottom: 27px; color: var(--white); }
  .office { font-size: 4.6px; font-weight: 500; }
  .locations { margin-top: 8px; font-size: 3.8px; letter-spacing: 0.18em; opacity: 0.85; }
  .brand-mark {
    position: absolute; right: 26px; bottom: 27px; display: flex; align-items: center; gap: 3px;
    font-size: 5px; font-weight: 600; color: var(--white);
  }
  .brand-mark::before { content: ""; width: 4px; height: 4px; background: var(--white); }

  /* opening */
  .opening-content { position: absolute; left: 16px; top: 26px; width: 146px; color: var(--white); }
  .opening-content .display { font-size: 18px; margin-top: 12px; }
  .quote { font-family: "Cormorant Garamond", serif; font-size: 9px; line-height: 1.15; margin-top: 24px; }
  .opening-content .rule { margin-top: 10px; }
  .opening-content .section-label { margin-top: 10px; }
  .section-label { font-size: 4.4px; letter-spacing: 0.16em; font-weight: 600; color: var(--gold); text-transform: uppercase; }
  .copy p { font-size: 4.3px; line-height: 1.45; margin-top: 6px; }
  .opening-content .copy p { color: rgba(255,255,255,0.88); }
  .folio { position: absolute; right: 14px; bottom: 9px; font-size: 4.5px; color: var(--white); letter-spacing: 0.1em; }

  /* meet */
  .title-block { position: absolute; left: 6px; top: 7px; width: 176px; height: 80px; background: var(--forest); padding: 20px 0 0 18px; }
  .title-block .display { font-size: 19px; margin-top: 10px; }
  .meet-content { position: absolute; left: 24px; top: 93px; width: 150px; color: var(--ink); }
  .experience { font-size: 4.4px; letter-spacing: 0.16em; font-weight: 700; }
  .sectors { list-style: none; margin-top: 14px; }
  .sectors li { font-size: 4.3px; font-weight: 600; margin-bottom: 6px; display: flex; align-items: center; gap: 5px; }
  .sectors li::before { content: ""; width: 2px; height: 2px; border-radius: 50%; background: var(--gold); }
  .meet-content .rule { margin-top: 6px; width: 55px; }
  .meet-content .section-label { margin-top: 13px; }
  .meet-content .copy p { font-weight: 700; color: var(--ink); }
</style>
</head>
<body>
<main class="spread">

  <section class="page page--cover">
    <div class="photo photo--agent-walking" role="img" aria-label="Portrait photograph of Maren Holt walking down a bright architectural staircase"></div>
    <div class="veil"></div>
    <div class="page-edge"></div>
    <div class="cover-content">
      <p class="eyebrow">Personal Profile</p>
      <h1 class="display">Maren<br>Holt</h1>
      <div class="rule"></div>
      <p class="cover-tagline">LUXURY WELLNESS PROPERTY</p>
      <p class="pillars"><span>PROPERTY</span><span>WELLNESS</span><span>LIFESTYLE</span></p>
    </div>
    <div class="cover-footer">
      <p class="office">Fenwick Dale Coastline Group</p>
      <p class="locations">HOPE ISLAND | SANCTUARY COVE | HELENSVALE</p>
    </div>
    <div class="brand-mark">Fenwick Dale</div>
  </section>

  <section class="page page--opening">
    <div class="photo photo--waterfront" role="img" aria-label="Lifestyle photograph of a waterfront pool with trees, a moored boat and sky reflections"></div>
    <div class="veil"></div>
    <div class="opening-content">
      <p class="eyebrow">The Opening Statement</p>
      <h2 class="display">Where<br>Property<br>Meets<br>Wellbeing</h2>
      <p class="quote">“A home is more than an address. It is the environment in which life unfolds.”</p>
      <div class="rule"></div>
      <p class="section-label">Opening Profile</p>
      <div class="copy">
        <p>I believe the most exceptional properties are not defined simply by their architecture, address or price.</p>
        <p>They are defined by how they make you feel.</p>
        <p>Natural light. Water views. Privacy. Green space. Indoor-outdoor living. A place to unwind, entertain, recharge and reconnect.</p>
        <p>My approach to luxury property brings these elements together — combining strategic real estate expertise with a genuine understanding of wellness, lifestyle and the way people want to live today.</p>
        <p>Because when we understand the lifestyle behind the property, we can create a more compelling story around it.</p>
      </div>
    </div>
    <span class="folio">02</span>
  </section>

  <section class="page page--meet">
    <div class="photo photo--agent-seated" role="img" aria-label="Portrait photograph of Maren Holt seated on a stone stool in a light interior"></div>
    <div class="title-block">
      <p class="eyebrow">Personal Profile</p>
      <h2 class="display">Meet Maren</h2>
    </div>
    <div class="meet-content">
      <p class="experience">20+ YEARS OF PROPERTY EXPERIENCE</p>
      <ul class="sectors">
        <li>Commercial</li>
        <li>Residential</li>
        <li>Project Sales</li>
        <li>Luxury &amp; Lifestyle Property</li>
      </ul>
      <div class="rule"></div>
      <p class="section-label">About Maren</p>
      <div class="copy">
        <p>With more than 20 years' experience across commercial, residential and project sales, I have built my career around relationships, strategic marketing and delivering exceptional outcomes for my clients.</p>
        <p>My approach is warm, considered and highly personal.</p>
        <p>I believe sellers deserve more than a listing campaign. They deserve a clear strategy, honest communication and an agent who understands what makes their property valuable — both financially and emotionally.</p>
        <p>Today, my focus is luxury lifestyle property across the Northern Gold Coast, with a particular passion for Hope Island, Sanctuary Cove and selected waterfront gated estates in Helensvale.</p>
      </div>
    </div>
  </section>

</main>
</body>
</html>
```